The name of my company is Tolmen Refacing LLC and I would like the sub text to say "Cabinet Refacing and Countertops". Have my name Dorian Tolmen, Owner / Sales, contact info: Cell: 360-555-0147 / Email: dorian.tolmen@quenmail.com

Simple, Clean, and Organized. With colors that will appeal to the eye.

Target Market(s)

Houses and Apartments

Industry/Entity Type

Cabinet Refacing

Contact Information for Business Card

Company name and sub text Dorian Tolmen - Owner / Sales, my cell phone number and email

Requirements
Must have
• Business name, my name / position, and my contact info
Nice to have
• Simple. Organized. Appealing to the eye

```html
<!DOCTYPE html>
<html lang="en">
<head>
<meta charset="utf-8">
<title>Tolmen Refacing LLC – Business Card</title>
<link rel="stylesheet" href="https://fonts.googleapis.com/css2?family=Montserrat:wght@400;500&display=swap">
<style>
  :root {
    --page-bg: #e5e5e5;
    --card-bg: #333333;
    --card-edge: #cfcfcf;
    --mint: #ccffcc;
  }
  * { margin: 0; padding: 0; box-sizing: border-box; }
  html, body {
    width: 1200px;
    height: 1200px;
    overflow: hidden;
    background: var(--page-bg);
    font-family: "Montserrat", sans-serif;
  }
  .business-card {
    position: absolute;
    left: 240px;
    top: 400px;
    width: 720px;
    height: 400px;
    background: var(--card-bg);
    border: 1px solid var(--card-edge);
    color: var(--mint);
    overflow: hidden;
  }
  .brand {
    position: absolute;
    left: 0;
    right: 0;
    top: 36px;
    display: flex;
    justify-content: center;
    align-items: center;
    gap: 10px;
  }
  .brand-square {
    width: 16px;
    height: 16px;
    background: var(--mint);
    flex: none;
  }
  .brand-text {
    display: flex;
    flex-direction: column;
    gap: 5px;
  }
  .brand-name {
    font-size: 14px;
    font-weight: 500;
    line-height: 1;
    letter-spacing: 0.2px;
  }
  .brand-tagline {
    font-size: 10px;
    font-weight: 400;
    line-height: 1;
    letter-spacing: 0.4px;
  }
  .person {
    position: absolute;
    left: 0;
    right: 0;
    top: 128px;
    text-align: center;
  }
  .person-name {
    font-size: 60px;
    font-weight: 500;
    line-height: 1;
    letter-spacing: 1px;
  }
  .person-role {
    margin-top: 8px;
    font-size: 26px;
    font-weight: 400;
    line-height: 1;
    letter-spacing: 0.4px;
  }
  .contact-list {
    position: absolute;
    left: 367px;
    top: 288px;
    list-style: none;
  }
  .contact-item {
    display: flex;
    align-items: center;
    gap: 12px;
    height: 22px;
    margin-bottom: 12px;
    font-size: 17px;
    font-weight: 400;
    letter-spacing: 0.2px;
  }
  .contact-icon {
    width: 21px;
    height: 21px;
    flex: none;
  }
  .accent-bar {
    position: absolute;
    left: 0;
    bottom: 0;
    width: 323px;
    height: 23px;
    background: var(--mint);
  }
</style>
</head>
<body>
  <section class="business-card">
    <div class="brand">
      <span class="brand-square"></span>
      <div class="brand-text">
        <span class="brand-name">Tolmen Refacing LLC</span>
        <span class="brand-tagline">Cabinet Refacing and Countertops</span>
      </div>
    </div>

    <div class="person">
      <h1 class="person-name">Dorian Tolmen</h1>
      <p class="person-role">Owner / Sales</p>
    </div>

    <ul class="contact-list">
      <li class="contact-item">
        <svg class="contact-icon" viewBox="0 0 21 21" aria-hidden="true">
          <rect x="0.5" y="0.5" width="20" height="20" fill="none" stroke="#ccffcc" stroke-width="1"/>
          <g transform="translate(3.9 3.9) scale(0.55)">
            <path d="M6.6 10.8c1.4 2.8 3.8 5.1 6.6 6.6l2.2-2.2c.3-.3.7-.4 1-.2 1.1.4 2.3.6 3.6.6.6 0 1 .4 1 1V20c0 .6-.4 1-1 1C10.6 21 3 13.4 3 4c0-.6.4-1 1-1h3.5c.6 0 1 .4 1 1 0 1.3.2 2.5.6 3.6.1.3 0 .7-.2 1z" fill="#ccffcc"/>
          </g>
        </svg>
        <span>360-555-0147</span>
      </li>
      <li class="contact-item">
        <svg class="contact-icon" viewBox="0 0 21 21" aria-hidden="true">
          <rect x="0.5" y="0.5" width="20" height="20" fill="none" stroke="#ccffcc" stroke-width="1"/>
          <rect x="5" y="6.5" width="11" height="8" rx="1" fill="#ccffcc"/>
          <path d="M5.5 7.2 L10.5 11 L15.5 7.2" fill="none" stroke="#333333" stroke-width="1.2"/>
        </svg>
        <span>dorian.tolmen@quenmail.com</span>
      </li>
    </ul>

    <div class="accent-bar"></div>
  </section>
</body>
</html>
```